Build an Online Store for Luxury Retail

Need a website/online store to sell retail luxury handmade items. Want a Clean, Efficient Design that combines colors graphics and processes that engage the user and portray a sense of high end luxury lifestyle while also going into detail about product. The website will feature mostly items for an affluent executive which could be purchased by the individual or by family members, friends or colleges who wish to purchase a gift with a high perceived value. The domain name is HarborlineGoods.com.

Examples of the products include: hand made writing instruments made from rare woods, and other unique materials gathered from around the world; personal hygiene (razors, toothbrushes, etc), pocket flashlights, USB drives, fine tools, other instruments for use in the office.

Some suggestions include: clean lines, Swiss-style, abstract linear drawings of tools, colors that are appropriate for hi-tech, luxury
items; however, please feel free to design this in your own way/style, since these are only suggestions.

The photo attached is an example of some of the pens, although this photo is NOT intended to show the color scheme. New photos, which are taken with a brighter background, and much lighter color scheme are in the process of being produced and will be ready in about a week. If you have any questions about this project, PLEASE feel free to email me with any questions or ideas.

```html
<!DOCTYPE html>
<html lang="en">
<head>
<meta charset="utf-8">
<title>Harborline Goods – Store Pages</title>
<link rel="stylesheet" href="https://fonts.googleapis.com/css2?family=Montserrat:wght@400;600;700;800&family=Open+Sans:wght@300;400;600;700&family=Crimson+Text:wght@400&display=swap">
<style>
:root{
  --ink:#222;
  --muted:#8a8a8a;
  --line:#d9d9d9;
  --green:#1fa37a;
  --hero:#6d6d74;
  --peach:#eeaa86;
  --white:#fff;
}
*{box-sizing:border-box;margin:0;padding:0}
html,body{width:1200px;height:4897px;overflow:hidden;background:var(--white)}
body{position:relative;font-family:"Open Sans",sans-serif;color:var(--ink)}
.abs{position:absolute}
.nav{position:absolute;display:flex;gap:38px;font:700 11px "Montserrat",sans-serif;letter-spacing:.5px}
.nav .active{border-bottom:2px solid currentColor;padding-bottom:8px}
.account{position:absolute;display:flex;align-items:center;gap:14px;font:400 11px "Open Sans",sans-serif}
.account .sep{width:1px;height:22px;background:currentColor;opacity:.5}
.icons{position:absolute;display:flex;gap:22px;align-items:center}
.brand{position:absolute;left:0;width:1200px;text-align:center;font:800 44px "Montserrat",sans-serif;letter-spacing:1px}
.side-tab{position:absolute;left:0;width:22px;height:26px;background:var(--green)}
.photo{position:absolute}
.hero-title{position:absolute;left:0;width:1200px;text-align:center;color:#fff;font:800 118px/112px "Montserrat",sans-serif;letter-spacing:2px}
.hero-rule{position:absolute;left:504px;width:184px;height:2px;background:#fff}
.lang{position:absolute;font:400 10px "Open Sans",sans-serif;letter-spacing:.5px;white-space:nowrap}
.pay{position:absolute;display:flex;gap:14px;font:700 8px "Open Sans",sans-serif;letter-spacing:.3px;white-space:nowrap}
.note{position:absolute;font:400 40px "Crimson Text",serif;color:#111;white-space:nowrap}
.tabs{position:absolute;font:400 17px "Open Sans",sans-serif;color:#aaa}
.tabs span{position:absolute;white-space:nowrap}
.tabs .on{color:#333;border-bottom:2px solid #333;padding-bottom:4px}
.ribbon{position:absolute;overflow:hidden}
.ribbon i{position:absolute;display:block;font:700 9px "Montserrat",sans-serif;font-style:normal;color:#fff;text-align:center;letter-spacing:1px;transform:rotate(-45deg)}
.quick{position:absolute;text-align:center;font:400 9px "Open Sans",sans-serif}
.filter-bar{position:absolute;left:0;width:1200px;text-align:center;font:700 10px "Montserrat",sans-serif;letter-spacing:.3px}
.card-hover{position:absolute;background:rgba(255,255,255,.93);border:4px solid #222;text-align:center}
.card-hover h4{font:700 11px "Montserrat",sans-serif;letter-spacing:.5px}
.card-hover .price{color:var(--green);font-size:11px;margin-top:10px}
.card-hover .btn{display:inline-block;margin-top:28px;border:3px double #333;padding:9px 22px;font:600 9px "Montserrat",sans-serif}
.sidebar{position:absolute;font-size:10px;color:#777;background:#fff}
.sidebar h5{font:400 11px "Open Sans",sans-serif;color:#555;display:flex;justify-content:space-between;border-bottom:1px solid #eee;padding-bottom:6px}
.sidebar ul{list-style:none;margin:14px 0 20px 0;line-height:20px;font-size:9px}
.center-text{position:absolute;text-align:center}
.label{position:absolute;text-align:center;font:400 11px "Open Sans",sans-serif;letter-spacing:.5px;color:#444}
.field{position:absolute;border:1px solid var(--line);background:#fff}
.btn-box{position:absolute;border:4px double #333;display:flex;align-items:center;justify-content:center;font:600 12px "Montserrat",sans-serif;background:#fff}
</style>
</head>
<body>

<!-- Home header -->
<nav class="nav" style="left:34px;top:38px;color:#333">
  <span class="active">HOME</span><span>SHOP</span><span>BLOG</span><span>PAGES</span>
</nav>
<div class="brand" style="top:16px">HARBORLINE</div>
<div class="account" style="left:882px;top:34px;color:#555"><span>My Account</span><span class="sep"></span><span>Checkout</span></div>
<div class="icons" style="left:1064px;top:32px">
  <svg width="20" height="18" viewBox="0 0 20 18"><path d="M10 16 2.5 8.6A4.3 4.3 0 0 1 10 3.4a4.3 4.3 0 0 1 7.5 5.2Z" fill="none" stroke="#222" stroke-width="2"/></svg>
  <svg width="18" height="18" viewBox="0 0 18 18"><circle cx="7.5" cy="7.5" r="5.5" fill="none" stroke="#222" stroke-width="2.2"/><path d="m11.5 11.5 5 5" stroke="#222" stroke-width="2.4"/></svg>
  <svg width="20" height="24" viewBox="0 0 20 24"><rect x="1" y="7" width="18" height="16" fill="#222"/><path d="M6 8V5a4 4 0 0 1 8 0v3" fill="none" stroke="#222" stroke-width="2"/><text x="10" y="19" font-size="8" fill="#fff" text-anchor="middle" font-family="Open Sans">0</text></svg>
</div>

<!-- Home hero -->
<div class="photo" role="img" aria-label="Hand-made rare-wood fountain pen on a dark grey backdrop" style="left:0;top:89px;width:1200px;height:508px;background:radial-gradient(ellipse 240px 420px at 600px 300px,#3e3b4a 0%,#575562 55%,var(--hero) 100%)"></div>
<div class="side-tab" style="top:108px"></div>
<div class="hero-rule" style="top:118px"></div>
<div class="hero-title" style="top:170px">WALNUT<br>PENS</div>
<div class="hero-rule" style="top:450px"></div>
<div class="lang" style="left:38px;top:543px;color:#ddd">ENGLISH &nbsp;▾</div>
<div class="pay" style="left:840px;top:553px;color:#ccc"><span>CORVEL</span><span>QUANTA</span><span>HELIO</span><span>TESSERA</span><span>LUMEN</span><span>BRIGHTLINE</span></div>

<div class="note" style="left:48px;top:622px">will popup on home screen</div>
<svg class="abs" style="left:200px;top:676px" width="100" height="74" viewBox="0 0 100 74"><path d="M6 6C30 24 48 40 80 62" fill="none" stroke="#111" stroke-width="6" stroke-linecap="round"/><path d="M54 62 84 66 78 38" fill="none" stroke="#111" stroke-width="6" stroke-linecap="round" stroke-linejoin="round"/></svg>

<div class="tabs" style="left:0;top:692px;width:1200px;height:30px">
  <span class="on" style="left:423px">Just Arrived</span>
  <span style="left:561px">Best Sellers</span>
  <span style="left:696px">Featured</span>
</div>

<div class="photo" role="img" aria-label="Ebony fountain pen" style="left:0;top:751px;width:191px;height:253px;background:linear-gradient(#f3f3f3,#e2dcd8 50%,#3a3a3a 90%)"></div>
<div class="photo" role="img" aria-label="Ivory-handled safety razor" style="left:191px;top:751px;width:209px;height:253px;background:linear-gradient(#f3f3f3,#ece6da 50%,#e6e0d4)"></div>
<div class="ribbon" style="left:191px;top:751px;width:120px;height:120px"><i style="left:-40px;top:30px;width:170px;height:32px;line-height:32px;background:var(--green)">SALE</i></div>
<div class="photo" role="img" aria-label="Olive-wood USB drive" style="left:400px;top:751px;width:200px;height:253px;background:linear-gradient(#f2f2f2,#d8c4b4 30%,#6e7f9a 50%,#cfae92 80%)"></div>
<div class="photo" role="img" aria-label="Brushed steel pocket flashlight" style="left:600px;top:751px;width:200px;height:253px;background:linear-gradient(#f3f3f3,#6d6d6d 45%,#8a8a8a 70%,#efefef)"></div>
<div class="photo" role="img" aria-label="Bamboo toothbrush set" style="left:800px;top:751px;width:200px;height:253px;background:linear-gradient(#f3f3f3,#d9d0c4 50%,#e8e4de)"></div>
<div class="photo" role="img" aria-label="Rosewood desk tool set" style="left:1000px;top:751px;width:200px;height:253px;background:linear-gradient(#f3f3f3,#4a2f2a 25%,#3b3b3b 70%)"></div>

<div class="lang" style="left:36px;top:1032px;color:#555">ENGLISH &nbsp;▾</div>
<div class="lang" style="left:34px;top:1048px;color:#aaa;font-size:8px">COPYRIGHT 2024 HARBORLINE GOODS. ALL RIGHTS RESERVED</div>
<div class="quick" style="left:560px;top:1028px;width:74px;color:#555"><div style="font-size:14px;letter-spacing:2px">○○○</div>QUICK SHOP</div>
<div class="pay" style="left:836px;top:1040px;color:#334"><span>CORVEL</span><span>QUANTA</span><span>HELIO</span><span>TESSERA</span><span>LUMEN</span><span>BRIGHTLINE</span></div>

<!-- Shop header -->
<div class="abs" style="left:0;top:1105px;width:1194px;height:361px;background:var(--peach)"></div>
<nav class="nav" style="left:34px;top:1142px;color:#fff"><span>HOME</span><span class="active">SHOP</span><span>BLOG</span><span>PAGES</span></nav>
<div class="account" style="left:868px;top:1138px;color:#fff"><span>My Account</span><span class="sep"></span><span>Checkout</span></div>
<div class="icons" style="left:1048px;top:1136px">
  <svg width="20" height="18" viewBox="0 0 20 18"><path d="M10 16 2.5 8.6A4.3 4.3 0 0 1 10 3.4a4.3 4.3 0 0 1 7.5 5.2Z" fill="none" stroke="#fff" stroke-width="2"/></svg>
  <svg width="18" height="18" viewBox="0 0 18 18"><circle cx="7.5" cy="7.5" r="5.5" fill="none" stroke="#fff" stroke-width="2.2"/><path d="m11.5 11.5 5 5" stroke="#fff" stroke-width="2.4"/></svg>
  <svg width="20" height="24" viewBox="0 0 20 24"><rect x="1" y="7" width="18" height="16" fill="#fff"/><path d="M6 8V5a4 4 0 0 1 8 0v3" fill="none" stroke="#fff" stroke-width="2"/><text x="10" y="19" font-size="8" fill="#eeaa86" text-anchor="middle" font-family="Open Sans">0</text></svg>
</div>
<div class="side-tab" style="top:1206px"></div>
<div class="photo" role="img" aria-label="Colourful gift bags in red, green, purple, orange and yellow" style="left:350px;top:1140px;width:490px;height:290px;border-radius:6px;background:linear-gradient(90deg,#d9344a 0%,#7aa63a 25%,#9a6f9c 45%,#ef6b2e 65%,#f0b42c 100%);opacity:.9"></div>
<div class="abs" style="left:0;top:1240px;width:1200px;text-align:center;color:#fff;font:800 78px 'Montserrat',sans-serif;letter-spacing:22px">SHOP</div>

<div class="filter-bar" style="top:1505px"><span style="font-size:15px;vertical-align:-2px">☰</span> &nbsp; FILTER PRODUCTS / SHOWING 1 - 12 OF 13 RESULTS</div>

<!-- Shop grid -->
<div class="photo" role="img" aria-label="Rosewood fountain pen product photo" style="left:11px;top:1565px;width:274px;height:343px;background:linear-gradient(#f2f2f2,#c9c9cc 30%,#f2f2f2)"></div>
<div class="card-hover" style="left:11px;top:1565px;width:274px;height:343px;padding-top:92px">
  <svg width="18" height="16" viewBox="0 0 20 18"><path d="M10 16 2.5 8.6A4.3 4.3 0 0 1 10 3.4a4.3 4.3 0 0 1 7.5 5.2Z" fill="none" stroke="#222" stroke-width="2"/></svg>
  <h4 style="margin-top:18px">ROSEWOOD FOUNTAIN PEN</h4>
  <div class="price">£80.00 – £85.00</div>
  <span class="btn">SELECT OPTIONS</span>
</div>
<div class="photo" role="img" aria-label="Burl-wood ballpoint pen in a navy case" style="left:310px;top:1565px;width:272px;height:343px;background:linear-gradient(#f2f2f2,#e5d2b8 20%,#27304f 45%,#7a2b3a 80%,#eee)"></div>
<div class="photo" role="img" aria-label="Rosewood desk tool set" style="left:607px;top:1565px;width:274px;height:343px;background:linear-gradient(#f2f2f2,#4a2f2a 25%,#3b3b3b 75%,#eee)"></div>
<div class="photo" role="img" aria-label="Ivory-handled safety razor" style="left:905px;top:1565px;width:274px;height:343px;background:linear-gradient(#f2f2f2,#ece6da 45%,#f0ece4)"></div>
<div class="ribbon" style="left:905px;top:1565px;width:120px;height:120px"><i style="left:-40px;top:30px;width:170px;height:32px;line-height:32px;background:var(--green)">SALE</i></div>

<div class="photo" role="img" aria-label="Anodised blue pocket flashlight" style="left:11px;top:1930px;width:274px;height:340px;background:linear-gradient(#f2f2f2,#4d6a8e 30%,#3e5678 80%,#eee)"></div>
<div class="ribbon" style="left:11px;top:1930px;width:120px;height:120px"><i style="left:-40px;top:30px;width:170px;height:32px;line-height:32px;background:#999;font-size:7px">OUT OF STOCK</i></div>
<div class="photo" role="img" aria-label="Ebony fountain pen" style="left:310px;top:1930px;width:272px;height:340px;background:linear-gradient(#f2f2f2,#e0cfc4 45%,#2e2e2e 80%)"></div>
<div class="photo" role="img" aria-label="Black leather pen roll with brass clasp" style="left:607px;top:1930px;width:274px;height:340px;background:linear-gradient(#f2f2f2,#222 35%,#c8b392 70%,#eee)"></div>
<div class="photo" role="img" aria-label="Steel multi-tool in a navy case" style="left:905px;top:1930px;width:274px;height:340px;background:linear-gradient(#f2f2f2,#34405e 35%,#7a8292 70%,#eee)"></div>

<div class="note" style="left:156px;top:2272px">with sidebar -&gt;price filter</div>

<!-- Sidebar variant -->
<div class="photo" role="img" aria-label="Rosewood fountain pen product photo" style="left:10px;top:2324px;width:209px;height:262px;background:linear-gradient(#f2f2f2,#c9c9cc 30%,#f2f2f2)"></div>
<div class="card-hover" style="left:10px;top:2324px;width:209px;height:262px;padding-top:64px;border-width:3px">
  <svg width="15" height="13" viewBox="0 0 20 18"><path d="M10 16 2.5 8.6A4.3 4.3 0 0 1 10 3.4a4.3 4.3 0 0 1 7.5 5.2Z" fill="none" stroke="#222" stroke-width="2"/></svg>
  <h4 style="margin-top:12px;font-size:9px">ROSEWOOD FOUNTAIN PEN</h4>
  <div class="price" style="font-size:9px;margin-top:6px">£80.00 – £85.00</div>
  <span class="btn" style="margin-top:18px;padding:6px 16px;font-size:7px">SELECT OPTIONS</span>
</div>
<div class="photo" role="img" aria-label="Burl-wood ballpoint pen in a navy case" style="left:238px;top:2324px;width:209px;height:262px;background:linear-gradient(#f2f2f2,#e5d2b8 20%,#27304f 45%,#7a2b3a 80%,#eee)"></div>
<div class="photo" role="img" aria-label="Rosewood desk tool set" style="left:466px;top:2324px;width:209px;height:262px;background:linear-gradient(#f2f2f2,#4a2f2a 25%,#3b3b3b 75%,#eee)"></div>
<div class="photo" role="img" aria-label="Ivory-handled safety razor" style="left:696px;top:2324px;width:209px;height:262px;background:linear-gradient(#f2f2f2,#ece6da 45%,#f0ece4)"></div>
<div class="ribbon" style="left:696px;top:2324px;width:90px;height:90px"><i style="left:-32px;top:22px;width:130px;height:26px;line-height:26px;background:var(--green);font-size:8px">SALE</i></div>

<aside class="sidebar" style="left:1014px;top:2278px;width:175px">
  <h5>Categories <span>-</span></h5>
  <ul><li>Pens</li><li>Razors</li><li>Flashlights</li><li>Drives</li><li>Tools</li></ul>
  <h5>Filter by Color <span>-</span></h5>
  <ul><li>Dark</li><li>Light</li></ul>
  <h5 style="border:0">Filter by price</h5>
  <svg width="175" height="16" viewBox="0 0 175 16" style="margin-top:8px;display:block"><rect x="6" y="7" width="162" height="3" fill="#1fa37a"/><rect x="2" y="3" width="8" height="10" rx="2" fill="#222"/><rect x="164" y="3" width="8" height="10" rx="2" fill="#222"/></svg>
  <div style="display:flex;justify-content:space-between;align-items:center;margin-top:8px;font-size:7px">
    <span>PRICE: £20 — £320</span>
    <span style="border:3px double #333;padding:2px 8px;color:#333;font-weight:700">FILTER</span>
  </div>
</aside>

<!-- Login -->
<div class="center-text" style="left:388px;top:2730px;width:400px;font:300 26px/40px 'Open Sans',sans-serif;color:#555">I'm an existing customer and<br>would like to login.</div>
<div class="label" style="left:321px;top:2858px;width:533px">USERNAME OR EMAIL *</div>
<div class="field" style="left:321px;top:2894px;width:533px;height:53px"></div>
<div class="label" style="left:321px;top:2972px;width:533px">PASSWORD *</div>
<div class="field" style="left:321px;top:3006px;width:533px;height:53px"></div>
<div class="abs" style="left:321px;top:3088px;font-size:11px;color:#444;display:flex;align-items:center;gap:14px"><span style="width:20px;height:20px;border:1px solid #bbb;display:inline-block"></span>Remember me</div>
<div class="abs" style="left:748px;top:3089px;font-size:12px;color:var(--green)">Lost Password?</div>
<div class="btn-box" style="left:534px;top:3145px;width:107px;height:49px">LOGIN</div>
<div class="center-text" style="left:300px;top:3202px;width:576px;font-size:11px;color:#888">Try our demo account - <b style="color:#444">username:</b> demo <b style="color:#444">password</b> demo</div>

<!-- Empty cart -->
<svg class="abs" style="left:513px;top:3337px" width="147" height="184" viewBox="0 0 147 184"><path d="M46 50V36a27 27 0 0 1 55 0v14" fill="none" stroke="#333" stroke-width="5"/><path d="M8 58h131l-6 122H14Z" fill="none" stroke="#333" stroke-width="5" stroke-linejoin="round"/></svg>
<div class="center-text" style="left:300px;top:3556px;width:576px;font:300 26px 'Open Sans',sans-serif;color:#555">Your cart is currently empty.</div>
<div class="btn-box" style="left:500px;top:3616px;width:175px;height:50px;font-size:12px">RETURN TO SHOP</div>

<!-- Contact -->
<div class="photo" role="img" aria-label="Street map showing the store location" style="left:0;top:3723px;width:396px;height:631px;background:linear-gradient(135deg,#f4f4f1,#e8efdc 40%,#f6f6f3 70%,#dfe9d2)"></div>
<div class="center-text" style="left:572px;top:3726px;width:480px;font:400 17px 'Open Sans',sans-serif;color:#333">We're here to help you find your new favorite things.</div>
<div class="center-text" style="left:450px;top:3775px;width:724px;font-size:10px;line-height:16px;color:#999">We are reasonable people and will try our best to work something out. If you are not completely happy with your new product, please send it back to us within 15 days for a full refund.</div>
<div class="center-text" style="left:572px;top:3848px;width:480px;font:400 22px 'Open Sans',sans-serif;color:#444">Contact Us</div>
<div class="label" style="left:572px;top:3893px;width:480px;font-size:10px">NAME</div>
<div class="field" style="left:572px;top:3919px;width:480px;height:42px"></div>
<div class="label" style="left:572px;top:3975px;width:480px;font-size:10px">E-MAIL</div>
<div class="field" style="left:572px;top:4003px;width:480px;height:42px"></div>
<div class="label" style="left:572px;top:4058px;width:480px;font-size:10px">YOUR MESSAGE</div>
<div class="field" style="left:572px;top:4086px;width:480px;height:160px"></div>
<div class="btn-box" style="left:738px;top:4272px;width:133px;height:37px;font-size:10px">SEND MESSAGE</div>

<div class="note" style="left:154px;top:4576px">Also will ad about us, services, blog as your requirement</div>

</body>
</html>
```